lumenweave project business card, interior design and decoration firm

I'm a young woman and I've just created my interior design consulting firm. I'm very inspired by brasilian design, italian design, argentinian spirit, I like pure forms, chic colors (blue specially) and raw stuffs (wood, glass,
I work with wines properties, boats and yachts dealers, private people. Elegant but inspired
It's very important to dedicate one side to this card to the name Lumenweave. I would like my name on the other side (Claire-Anne Vobrel), my mail cavobrel@postvane.fr, my number + 33 6 91 35 20 86

Target Market(s)

middle and upper class, young people,

Contact Information for Business Card

Font styles to use
Sans Serif

Colors
0255a3
85abd2
000000
fdfdfd
86cfc6
fdf0f6
00a990
f04a50

Requirements
Must have
• The name Lumenweave, my name my number and mail one or two colors max, one logo if it's possible. AND uder The name Lumenweave "Cabinet de conseil en aménagement intérieur"

```html
<!DOCTYPE html>
<html lang="fr">
<head>
<meta charset="utf-8">
<title>Lumenweave — business card</title>
<link rel="stylesheet" href="https://fonts.googleapis.com/css2?family=Questrial&family=Mulish:wght@400;600;700&display=swap">
<style>
  :root {
    --backdrop: #e8e8eb;
    --card-front: #fdf0f6;
    --card-back: #fdfdfd;
    --ink: #000000;
    --ink-soft: #1a1a1a;
    --card-shadow: rgba(0, 0, 0, 0.12);
  }
  * { box-sizing: border-box; margin: 0; padding: 0; }
  html, body {
    width: 1200px;
    height: 880px;
    overflow: hidden;
    background: var(--backdrop);
  }
  .canvas {
    position: relative;
    width: 1200px;
    height: 880px;
  }
  .card {
    position: absolute;
    width: 630px;
    height: 360px;
    border-radius: 24px;
    box-shadow: 0 10px 28px var(--card-shadow);
  }
  .card--front {
    left: 170px;
    top: 50px;
    background: var(--card-front);
  }
  .card--back {
    left: 400px;
    top: 470px;
    background: var(--card-back);
  }
  .brand {
    position: absolute;
    left: 118px;
    top: 128px;
  }
  .brand__name {
    font-family: "Questrial", "Century Gothic", sans-serif;
    font-size: 82px;
    font-weight: 400;
    line-height: 1;
    letter-spacing: -1px;
    color: var(--ink);
  }
  .brand__tagline {
    margin-top: 10px;
    font-family: "Mulish", "Century Gothic", sans-serif;
    font-size: 14px;
    font-weight: 700;
    letter-spacing: 0.2px;
    color: var(--ink);
    white-space: nowrap;
  }
  .contact {
    position: absolute;
    left: 238px;
    top: 138px;
    color: var(--ink);
  }
  .contact__name {
    font-family: "Questrial", "Century Gothic", sans-serif;
    font-size: 25px;
    line-height: 1.1;
    margin-bottom: 14px;
  }
  .contact__line {
    font-family: "Mulish", "Century Gothic", sans-serif;
    font-size: 15px;
    line-height: 1.45;
    color: var(--ink-soft);
  }
  .contact__label { font-weight: 700; }
</style>
</head>
<body>
  <main class="canvas">
    <section class="card card--front" aria-label="Card front">
      <div class="brand">
        <h1 class="brand__name">Lumenweave</h1>
        <p class="brand__tagline">Cabinet de conseil en aménagement intérieur</p>
      </div>
    </section>

    <section class="card card--back" aria-label="Card back">
      <div class="contact">
        <h2 class="contact__name">Claire-Anne Vobrel</h2>
        <p class="contact__line"><span class="contact__label">P:</span> + 33 6 91 35 20 86</p>
        <p class="contact__line"><span class="contact__label">E:</span> cavobrel@postvane.fr</p>
      </div>
    </section>
  </main>
</body>
</html>
```